Website - add Lead Capture and Funnel Pages - New Fresh Design

For design: please recreate this landing page: https://brightlanehaul.com/carrier-program-signup/
We need a fresh new look for our website brightlanehaul.com - currently in Zoru, and possibly move to Pagecraft. We need new landing pages, funnel designs, and lead capture pages.

Prefer someone that has experience with Landing Pages and Lead Capture.

The target market is: Owner Operators of Trucking Companies. In other words, a person that owns an 18 wheeler truck to transport materials, that also drives it. These owners, need support, and we offer support to them in order to keep them compliant with Bureau of Freight Oversight regulations in the United States.

Target Market(s)

Truckers in the USA who own and drive for themselves 18 wheelers...

Industry/Entity Type

Business to Business Services, Trucking

Coding

Coded - Design and coding required

Number of Pages Required

5+ page

Font styles to use
Sans Serif

Colors
0054AA
0677BA
7BADD7
CADEEF
E8F1F8

Requirements
Must have
• Lead Pages, Lead Capture, Funnel Creation, On Page SEO using Rankwell Toolkit, Blog Page area, Clear Call to Actions, Mobile Friendly.
Nice to have
• Keep current color scheme, follow logo colors. Nice to have custom photography, and video explainers.

```html
<!DOCTYPE html>
<html lang="en">
<head>
<meta charset="utf-8">
<title>Brightlane Haul – Compliance Made Simple</title>
<link href="https://fonts.googleapis.com/css2?family=Montserrat:wght@400;500;600;700&family=Roboto:wght@400;500;700&display=swap" rel="stylesheet">
<style>
:root{
  --brand:#0054AA;
  --brand-mid:#0677BA;
  --brand-light:#7BADD7;
  --brand-pale:#CADEEF;
  --brand-tint:#E8F1F8;
  --brand-deep:#003d7d;
  --ink:#14263b;
  --text:#4d5b6b;
  --line:#CADEEF;
  --band:#0a3a6e;
  --footer:#0b2340;
  --footer-deep:#071a31;
  --white:#fff;
}
*{box-sizing:border-box;margin:0;padding:0}
html,body{width:1200px;height:5343px;overflow:hidden}
body{font-family:"Roboto",Arial,sans-serif;color:var(--text);background:var(--white)}
section,header,footer{position:relative;width:1200px;overflow:hidden}
.abs{position:absolute}
h1,h2,h3,.heading{font-family:"Montserrat",Arial,sans-serif;color:var(--ink)}
.accent{color:var(--brand)}
.btn{display:inline-flex;align-items:center;justify-content:center;font-family:"Montserrat",sans-serif;font-weight:600;font-size:11px;letter-spacing:.5px;text-transform:uppercase;color:var(--white);border-radius:3px}
.btn-brand{background:var(--brand)}

/* header */
.site-header{height:90px;background:var(--white);box-shadow:0 2px 6px rgba(0,40,90,.1);z-index:2}
.topbar{position:absolute;right:114px;top:0;height:30px;width:390px;background:var(--brand-tint);display:flex;align-items:center;justify-content:space-around;font-size:10.5px;color:#2b3d52}
.topbar span{display:flex;align-items:center;gap:6px}
.dot-ic{width:16px;height:16px;border-radius:50%;background:var(--brand);display:inline-flex;align-items:center;justify-content:center}
.brand{position:absolute;left:96px;top:30px;display:flex;align-items:center;gap:8px}
.brand-mark{width:12px;height:12px;background:var(--brand)}
.brand-name{font-family:"Montserrat",sans-serif;font-weight:600;font-size:19px;letter-spacing:1.5px;color:var(--ink)}
.main-nav{position:absolute;left:410px;top:56px;display:flex;gap:38px;font-family:"Montserrat",sans-serif;font-size:10.5px;font-weight:500;color:#2b3d52}
.main-nav .active{color:var(--ink);border-bottom:2px solid var(--brand);padding-bottom:6px}
.login{position:absolute;left:940px;top:46px;width:138px;height:30px;font-size:10.5px;text-transform:none;gap:6px}

/* hero */
.hero{height:647px}
.hero-photo{position:absolute;inset:0;background:linear-gradient(100deg,#0c2340 0%,#1f4a7a 35%,#0677BA 62%,#0054AA 78%,#2a4a6c 100%)}
.hero-shade{position:absolute;inset:0;background:linear-gradient(90deg,rgba(0,20,45,.5),rgba(0,20,45,0) 60%)}
.hero-eyebrow{left:113px;top:180px;font-family:"Montserrat",sans-serif;font-size:22px;letter-spacing:3px;color:var(--white)}
.hero-title{left:110px;top:210px;font-size:56px;line-height:58px;font-weight:600;color:var(--white);letter-spacing:1px}
.hero-sub{left:118px;top:340px;font-size:17px;line-height:27px;color:var(--white);font-family:"Montserrat",sans-serif}
.hero-btn-dark{left:135px;top:418px;width:142px;height:44px;background:rgba(8,30,60,.75);border-radius:22px}
.hero-btn-brand{left:305px;top:418px;width:182px;height:44px;border-radius:22px}
.arrow{top:250px}

/* approach */
.approach{height:660px}
.section-title{text-align:center;font-size:30px;line-height:40px;font-weight:600;letter-spacing:.5px}
.section-sub{text-align:center;font-size:17px;color:#3a4a5c}
.approach .section-title{position:absolute;left:0;right:0;top:70px}
.approach .section-sub{position:absolute;left:0;right:0;top:170px}
.feature{position:absolute;top:263px;width:240px;height:295px;background:var(--white);box-shadow:0 4px 18px rgba(0,50,110,.12);padding:34px 38px}
.feature .ic{width:54px;height:54px;border-radius:50%;background:var(--brand-tint);display:flex;align-items:center;justify-content:center;margin-bottom:30px}
.feature h3{font-size:16px;font-weight:600;margin-bottom:12px}
.feature p{font-size:11px;line-height:17.5px;color:var(--text)}
.feature.featured{top:251px;height:307px;background:linear-gradient(150deg,#0677BA 0%,#0054AA 60%,#004893 60%,#004893 100%);z-index:1}
.feature.featured .ic{background:var(--brand-deep)}
.feature.featured h3,.feature.featured p{color:var(--white)}

/* how to order */
.order{height:683px;background:linear-gradient(var(--band) 0 513px,var(--white) 513px)}
.order .section-title{position:absolute;left:0;right:0;top:68px;color:var(--white);font-size:34px}
.order .section-sub{position:absolute;left:0;right:0;top:123px;color:var(--brand-tint)}
.video-accent{left:236px;top:186px;width:165px;height:6px;background:var(--brand-light)}
.video-accent-v{left:236px;top:186px;width:6px;height:120px;background:var(--brand-light)}
.video-shadow{left:252px;top:209px;width:690px;height:413px;background:var(--brand-pale)}
.video{left:242px;top:193px;width:690px;height:413px;background:linear-gradient(160deg,#2c4766 0%,#4d6f95 40%,#0677BA 70%,#0c2340 100%)}
.video-caption{left:242px;top:380px;width:690px;text-align:center;font-family:"Montserrat",sans-serif;font-size:25px;line-height:33px;color:var(--white);letter-spacing:1px}
.play{left:550px;top:360px}

/* women owned */
.women{height:500px}
.hex-photo{left:120px;top:25px}
.women h2{left:640px;top:85px;width:470px;font-size:24px;line-height:33px;font-weight:600;letter-spacing:.5px}
.women .rule{left:642px;top:195px;width:70px;height:3px;background:var(--brand)}
.women p{left:640px;top:220px;width:440px;font-size:17px;line-height:24px;color:var(--text)}
.women .btn{left:642px;top:318px;width:155px;height:40px}

/* who we serve */
.serve{height:570px;background:linear-gradient(90deg,var(--brand-tint),#f4f8fc 45%,var(--brand-tint))}
.serve h2{left:100px;top:150px;font-size:31px;font-weight:600;letter-spacing:.5px}
.serve .lead{left:100px;top:228px;width:390px;font-size:17px;line-height:28px;color:var(--text)}
.tile{position:absolute;width:258px;height:190px;display:flex;flex-direction:column;justify-content:flex-end;padding:20px 28px;color:var(--white);font-family:"Montserrat",sans-serif;font-weight:600;font-size:15px;letter-spacing:.5px}
.tile.entre{left:518px;top:70px;background:linear-gradient(160deg,#0677BA,#0054AA);justify-content:flex-start;padding-top:62px}
.tile.entre p{font-family:"Roboto",sans-serif;font-weight:400;font-size:10px;line-height:13px;margin-top:12px;letter-spacing:0;opacity:.92}
.tile.small{left:518px;top:270px;background:linear-gradient(160deg,#9cb6cf,#3d5673)}
.tile.solo{left:790px;top:125px;background:linear-gradient(160deg,#b9cbdc,#2f4660)}
.tile.indiv{left:790px;top:330px;background:linear-gradient(160deg,#cadeef,#3f5c78)}

/* compliance services */
.services{height:695px}
.services .section-title{position:absolute;left:0;right:0;top:62px}
.svc-grid{position:absolute;left:140px;top:190px;width:965px;display:grid;grid-template-columns:repeat(4,1fr);grid-template-rows:195px 185px}
.svc{text-align:center;padding:20px 24px 0;border-right:1px solid var(--line)}
.svc:nth-child(4n){border-right:none}
.svc:nth-child(-n+4){border-bottom:1px solid var(--line)}
.svc.raised{background:var(--white);box-shadow:0 4px 16px rgba(0,50,110,.14);border:none;padding-top:22px}
.svc svg{display:block;margin:0 auto 18px}
.svc h3{font-family:"Roboto",sans-serif;font-size:13px;font-weight:500;color:var(--ink);margin-bottom:10px}
.svc p{font-size:9.5px;line-height:17px;color:#7a8796}

/* news */
.news{height:605px;background:var(--brand-tint)}
.news h2{left:120px;top:68px;font-size:30px;font-weight:600;letter-spacing:.5px}
.news-main{left:120px;top:130px;width:482px;height:380px;background:linear-gradient(170deg,#7BADD7 0%,#CADEEF 45%,#2f5a86 62%,#0c2340 100%)}
.news-main .date,.news-side .date{display:inline-block;background:var(--ink);color:var(--white);font-size:9.5px;padding:4px 10px;font-weight:500}
.news-main .cap{position:absolute;left:50px;bottom:30px;width:400px}
.news-main .cap .date{background:var(--brand)}
.news-main h3{color:var(--white);font-size:16px;line-height:20px;margin-top:10px;font-weight:600}
.news-side{left:610px;width:445px;height:182px;background:var(--white);display:flex}
.news-side .ph{width:215px;height:100%;flex:none}
.news-side .body{padding:16px 24px}
.news-side h4{font-size:11.5px;color:var(--ink);font-weight:700;margin:12px 0 8px}
.news-side p{font-size:11px;line-height:19px;color:#7a8796}

/* quote */
.quote{height:500px;background:linear-gradient(110deg,#0054AA,#00468f 55%,#0677BA)}
.quote h2{position:absolute;left:0;right:0;top:88px;text-align:center;color:var(--white);font-size:30px;font-weight:600;letter-spacing:1px}
.field{position:absolute;background:var(--white);height:45px;font-size:12px;color:#6b7988;padding:14px 18px}
.quote .send{left:505px;top:380px;width:190px;height:45px;border:2px solid var(--white);background:transparent;font-size:13px}

/* footer */
.site-footer{height:393px;background:var(--footer)}
.fcol{position:absolute;top:60px;border-left:3px solid var(--brand-mid);padding-left:22px;height:220px}
.fcol h4{font-family:"Montserrat",sans-serif;color:var(--white);font-size:15px;font-weight:600;letter-spacing:.5px;margin-bottom:26px}
.fcol p,.fcol li{font-size:9.5px;line-height:17.5px;color:var(--brand-pale);list-style:none}
.fcol strong{color:var(--white);font-weight:500}
.office{display:flex;gap:14px;margin-bottom:20px}
.office svg{flex:none}
.copyright{position:absolute;left:0;right:0;bottom:0;height:55px;background:var(--footer-deep);text-align:center;font-size:9.5px;color:var(--brand-light);line-height:55px}
</style>
</head>
<body>

<header class="site-header">
  <div class="topbar">
    <span><i class="dot-ic"><svg width="8" height="8" viewBox="0 0 10 10"><path d="M2 1l2 2-1 1.2a6 6 0 0 0 2.8 2.8L7 6l2 2-1.3 1.4C4.5 9 1 5.5.6 2.3z" fill="#fff"/></svg></i>Toll Free 800-555-0142</span>
    <span><i class="dot-ic"><svg width="9" height="7" viewBox="0 0 10 7"><rect x=".5" y=".5" width="9" height="6" fill="none" stroke="#fff"/><path d="M.5.5l4.5 3.5L9.5.5" fill="none" stroke="#fff"/></svg></i>sales@brightlanehaul.com</span>
  </div>
  <div class="brand"><span class="brand-mark"></span><span class="brand-name">BRIGHTLANE HAUL</span></div>
  <nav class="main-nav">
    <span class="active">OUR SERVICES</span><span>NCRBA COMPLIANCE</span><span>INDUSTIRES WE SERVE</span><span>CONTACT US</span>
  </nav>
  <span class="btn btn-brand login"><svg width="11" height="11" viewBox="0 0 12 12"><circle cx="6" cy="3.5" r="3" fill="#fff"/><path d="M0 12c0-4 3-5.5 6-5.5s6 1.5 6 5.5z" fill="#fff"/></svg>Corporate Login</span>
</header>

<section class="hero">
  <div class="hero-photo" role="img" aria-label="Truck driver in sunglasses and cap looking out of a semi-truck cab window"></div>
  <div class="hero-shade"></div>
  <div class="abs hero-eyebrow">BRIGHTLANE HAUL</div>
  <h1 class="abs hero-title">COMPLIANCE<br>MADE SIMPLE</h1>
  <p class="abs hero-sub">Pre-Employment Screening: Backgrounds -<br>Drug Testing - Driving Records</p>
  <span class="abs btn hero-btn-dark">Order A Report</span>
  <span class="abs btn btn-brand hero-btn-brand">Join Consortium</span>
  <svg class="abs arrow" style="left:30px" width="24" height="48" viewBox="0 0 24 48"><path d="M20 2L4 24l16 22" fill="none" stroke="#fff" stroke-width="2"/></svg>
  <svg class="abs arrow" style="left:1146px" width="24" height="48" viewBox="0 0 24 48"><path d="M4 2l16 22L4 46" fill="none" stroke="#fff" stroke-width="2"/></svg>
</section>

<section class="approach">
  <h2 class="section-title">THE SMART &amp; AFFORDABLE APPROACH TO<br><span class="accent">EMPLOYMENT SCREENING</span></h2>
  <p class="section-sub">We take a complicated process and make it easy.</p>

  <div class="feature" style="left:113px">
    <div class="ic"><svg width="26" height="26" viewBox="0 0 26 26" fill="none" stroke="#0054AA" stroke-width="1.5"><rect x="4" y="3" width="18" height="20"/><path d="M8 9h10M8 13h10M8 17h6"/></svg></div>
    <h3>Data Entry Free!</h3>
    <p>No more paper forms, data, or emails back and forth. All we need is the applicants email, we take care of the rest.</p>
  </div>
  <div class="feature featured" style="left:355px">
    <div class="ic"><svg width="26" height="26" viewBox="0 0 26 26" fill="none" stroke="#fff" stroke-width="1.5"><rect x="3" y="5" width="20" height="15"/><path d="M7 10h12M7 14h8M9 23h8"/></svg></div>
    <h3>FCRA Compliant</h3>
    <p>We make sure the process is FCRA compliant. Electronic Signatures, Consent Forms, Disclosure and Court Verifications.</p>
  </div>
  <div class="feature" style="left:598px">
    <div class="ic"><svg width="26" height="26" viewBox="0 0 26 26" fill="none" stroke="#0054AA" stroke-width="1.5"><circle cx="15" cy="10" r="6"/><path d="M15 7v6M13 9h4M4 23l7-7"/></svg></div>
    <h3>Simple Pricing</h3>
    <p>Whether you need a background on yourself or someone else, one report or multiple services, we offer affordable Nationwide Services 24/7.</p>
  </div>
  <div class="feature" style="left:843px">
    <div class="ic"><svg width="26" height="26" viewBox="0 0 26 26" fill="none" stroke="#0054AA" stroke-width="1.5"><rect x="4" y="5" width="18" height="12"/><path d="M2 20h22M8 9h10M8 13h6"/></svg></div>
    <h3>Online Reporting</h3>
    <p>Track applicant status, and get notifications about report status right to your email. View reports 24/7 in your Secure Dashboard.</p>
  </div>
</section>

<section class="order">
  <h2 class="section-title">HOW TO ORDER HERE</h2>
  <p class="section-sub">We take a complicated process and make it easy.</p>
  <div class="abs video-shadow"></div>
  <div class="abs video-accent"></div>
  <div class="abs video-accent-v"></div>
  <div class="abs video" role="img" aria-label="Explainer video still of a businesswoman working on a laptop in front of a city skyline"></div>
  <div class="abs video-caption">REDUCE TIME TO HIRE<br>WITH AUTOMATED WORKFLOWS BETWEEN</div>
  <svg class="abs play" width="76" height="76" viewBox="0 0 76 76"><circle cx="38" cy="38" r="35" fill="#fff" stroke="#0054AA" stroke-width="4"/><path d="M30 24l22 14-22 14z" fill="#0054AA"/></svg>
</section>

<section class="women">
  <svg class="abs hex-photo" width="465" height="405" viewBox="0 0 465 405" role="img" aria-label="Smiling woman truck driver in a cap sitting at the wheel of her truck">
    <defs><linearGradient id="hexFill" x1="0" y1="0" x2="1" y2="1"><stop offset="0" stop-color="#2f4660"/><stop offset=".45" stop-color="#7BADD7"/><stop offset="1" stop-color="#0054AA"/></linearGradient></defs>
    <polygon points="116,2 349,2 463,202 349,403 116,403 2,202" fill="none" stroke="#0054AA" stroke-width="1.5"/>
    <polygon points="127,22 338,22 441,202 338,383 127,383 24,202" fill="url(#hexFill)"/>
  </svg>
  <h2 class="abs">BRIGHTLANE HAUL IS A WOMEN OWNED, CERTIFIED WBE, MBE &amp; DBE IN AZ, CA, TX &amp; NV</h2>
  <div class="abs rule"></div>
  <p class="abs">Lorem ipsum dolor sit amet, consectetur adipiscing elit, sed do eiusmod tempor incididunt ut labore et dolore magna aliqua.</p>
  <span class="abs btn btn-brand">Certifications</span>
</section>

<section class="serve" aria-label="Who we serve">
  <h2 class="abs">WHO WE SERVE</h2>
  <p class="abs lead">Lorem ipsum dolor sit amet, consectetur adipiscing elit, sed do eiusmod tempor incididunt ut labore et dolore magna aliqua Lorem ipsum dolor sit</p>
  <div class="tile entre">ENTREPRENEUR<p>We serve the Entrepreneur who wants to get the process started with the applicant and leaves the workflow up to usWe serve the HR Manager</p></div>
  <div class="tile small" role="img" aria-label="Small business team smiling in an office">SMALL BUSINESS</div>
  <div class="tile solo" role="img" aria-label="Two business people talking">SOLOPRENEUR</div>
  <div class="tile indiv" role="img" aria-label="Smiling woman with arms crossed">INDIVIDUAL</div>
</section>

<section class="services">
  <h2 class="section-title">COMPLIANCE SERVICES FOR<br><span class="accent">MOTOR CARRIERS</span></h2>
  <div class="svc-grid">
    <div class="svc">
      <svg width="40" height="40" viewBox="0 0 40 40" fill="none" stroke="#0054AA" stroke-width="1.5"><rect x="4" y="6" width="32" height="28"/><path d="M4 13h32M10 19h8M10 25h8M22 19h8M22 25h8"/></svg>
      <h3>Clearinghouse Enrollment</h3>
      <p>NCRBA Clearinghouse launched Jan 2020 and many carriers have yet to enroll in the Clearinghouse.</p>
    </div>
    <div class="svc raised">
      <svg width="40" height="40" viewBox="0 0 40 40" fill="none" stroke="#0054AA" stroke-width="1.5"><circle cx="20" cy="11" r="6"/><path d="M8 36c0-9 5-14 12-14M24 34l10-10 3 3-10 10h-3z"/></svg>
      <h3>BOC3 Registration</h3>
      <p>BOC3 is required for each MC that has their own Authority. The BOC3 designates an Agent per State for</p>
    </div>
    <div class="svc">
      <svg width="40" height="40" viewBox="0 0 40 40" fill="none" stroke="#0054AA" stroke-width="1.5"><rect x="5" y="7" width="26" height="28" rx="2"/><path d="M16 26l2-6 14-14 4 4-14 14z"/></svg>
      <h3>IRP Registration</h3>
      <p>Registration reciprocity agreement among the US and Canadian Provinces, which provides payment of license fees</p>
    </div>
    <div class="svc">
      <svg width="40" height="40" viewBox="0 0 40 40" fill="none" stroke="#0054AA" stroke-width="1.5"><path d="M8 4h18l6 6v26H8z"/><path d="M13 14h14M13 20h14M13 26h9"/></svg>
      <h3>SCAC Registration</h3>
      <p>A registration code used to identify transportation companies doing business with military, government,</p>
    </div>
    <div class="svc">
      <svg width="40" height="40" viewBox="0 0 40 40" fill="none" stroke="#0054AA" stroke-width="1.5"><circle cx="25" cy="13" r="9"/><path d="M23 10a2.5 2.5 0 1 1 3 3v2M25 18v1"/><rect x="4" y="20" width="16" height="16"/><path d="M8 26h8M8 31h8"/></svg>
      <h3>Driver Clearinghouse Query</h3>
      <p>NCRBA Clearinghouse launched Jan 2020 and many carriers have yet to enroll in the Clearinghouse.</p>
    </div>
    <div class="svc">
      <svg width="40" height="40" viewBox="0 0 40 40" fill="none" stroke="#0054AA" stroke-width="1.5"><rect x="5" y="5" width="30" height="24"/><circle cx="20" cy="15" r="5"/><path d="M13 35h14M20 29v6"/></svg>
      <h3>UCR Registration</h3>
      <p>BOC3 is required for each MC that has their own Authority. The BOC3 designates an Agent per State for</p>
    </div>
    <div class="svc">
      <svg width="40" height="40" viewBox="0 0 40 40" fill="none" stroke="#0054AA" stroke-width="1.5"><rect x="6" y="4" width="24" height="32"/><path d="M11 11h14M11 17h14M11 23h8M22 30l12-14 3 3-12 14h-3z"/></svg>
      <h3>IFTA Registration</h3>
      <p>Registration reciprocity agreement among the US and Canadian Provinces, which provides payment of license fees</p>
    </div>
    <div class="svc">
      <svg width="40" height="40" viewBox="0 0 40 40" fill="none" stroke="#0054AA" stroke-width="1.5"><path d="M8 32L30 10M14 12l14 14M26 6l8 8-4 4-8-8zM6 34l4-8 4 4z"/></svg>
      <h3>Drug Testing Consortium</h3>
      <p>A registration code used to identify transportation companies doing business with military, government,</p>
    </div>
  </div>
</section>

<section class="news">
  <h2 class="abs">LATEST <span class="accent">NEWS</span></h2>
  <article class="abs news-main" role="img" aria-label="Row of semi-trucks parked at a depot under a blue sky">
    <div class="cap"><span class="date">28 MAY 2021</span><h3>Lorem ipsum dolor sit amet, consectetur adipiscing elit, sed do eiusmod tempor</h3></div>
  </article>
  <article class="abs news-side" style="top:130px">
    <div class="ph" role="img" aria-label="Driver leaning out of a truck cab door" style="background:linear-gradient(160deg,#E8F1F8,#7BADD7 60%,#2f4660)"></div>
    <div class="body"><span class="date">19 MAY 2021</span><h4>Lorem ipsum dolor sit</h4><p>Duis aute irure dolor in reprehenderit in voluptate velit esse cillum dolore eu fugiat</p></div>
  </article>
  <article class="abs news-side" style="top:325px">
    <div class="ph" role="img" aria-label="Woman driver smiling at the wheel of a truck" style="background:linear-gradient(160deg,#4d6f95,#1c3654 55%,#0677BA)"></div>
    <div class="body"><span class="date">18 MAY 2021</span><h4>Lorem ipsum dolor sit</h4><p>Duis aute irure dolor in reprehenderit in voluptate velit esse cillum dolore eu fugiat</p></div>
  </article>
</section>

<section class="quote">
  <h2>REQUEST A QUOTE</h2>
  <div class="field" style="left:268px;top:160px;width:325px">First Name</div>
  <div class="field" style="left:603px;top:160px;width:325px">Last Name</div>
  <div class="field" style="left:268px;top:212px;width:325px">Phone Number</div>
  <div class="field" style="left:603px;top:212px;width:325px">Email address</div>
  <div class="field" style="left:268px;top:264px;width:660px;height:86px">Message</div>
  <span class="abs btn send">Send Enquiry</span>
</section>

<footer class="site-footer">
  <div class="fcol" style="left:105px;width:240px">
    <h4>OUR OFFICE</h4>
    <div class="office"><svg width="22" height="22" viewBox="0 0 22 22"><circle cx="11" cy="11" r="11" fill="#fff"/><path d="M11 5a4 4 0 0 0-4 4c0 3 4 8 4 8s4-5 4-8a4 4 0 0 0-4-4z" fill="#0b2340"/></svg><p>418 Cedar Row, Ste B Harlow,<br>AZ Florida Office</p></div>
    <div class="office"><svg width="22" height="22" viewBox="0 0 22 22"><circle cx="11" cy="11" r="11" fill="#fff"/><path d="M11 5a4 4 0 0 0-4 4c0 3 4 8 4 8s4-5 4-8a4 4 0 0 0-4-4z" fill="#0b2340"/></svg><p>905 Lakeview Pkwy, Ste<br>236, Ardena, FL</p></div>
  </div>
  <div class="fcol" style="left:362px;width:210px">
    <h4>CONTACT US</h4>
    <p><strong>Customer Inquiry</strong><br>Toll Free: 800-555-0142<br>Phone: 602-555-0116<br>Fax: 602-555-0118<br>sales@brightlanehaul.com<br>consortium@brightlanehaul.com</p>
  </div>
  <div class="fcol" style="left:588px;width:240px">
    <h4>QUICK LINKS</h4>
    <ul><li>Drug Testing Needs Assessment</li><li>WorkCheck Client Sign-Up</li><li>WorkCheck – I9 Entry</li><li>Background Consent E-Form</li><li>Affiliate Referral Tracking</li><li>99 Drug Testing Clinics</li><li>Blog</li></ul>
  </div>
  <div class="fcol" style="left:845px;width:240px">
    <h4>PDF DOWNLOADS</h4>
    <ul><li>Applicant Consent Form PDF</li><li>Applicant Consent Form Word</li><li>FCRA Summary of Rights</li></ul>
  </div>
  <div class="copyright">© 2020 Brightlane Haul Background Checks &amp; Drug Testing</div>
</footer>

</body>
</html>
```